"Maple Hollow" red wine label design

We are a Sydney based company. We need to design a wine label for a Australian red wine.
Front label include following info:
Our brand: "Maple Hollow";
Product name: "Shiraz 2016";
In the bottom with small font: "Wine of Australia", "750ml"
Back label:
the back label would need to be consistent with the front label, with space for one paragraph of tasting notes, and ingredient info etc.
we would like to use white, gold and blue in this label. It should make customer feel the magical and beautiful moment of starry night.

We also need a logo design for the wine brand: "Maple Hollow"

I have attached a few wine bottle that used blue to give you some inspirations.

We need the design in AI file format.

Target Market(s)

both men and women

Industry/Entity Type

It Company

Logo Text

Maple Hollow

Requirements
Nice to have
• gold borderline, words; use of blue and white

```html
<!DOCTYPE html>
<html lang="en">
<head>
<meta charset="utf-8">
<title>Maple Hollow Shiraz 2016 – Label</title>
<link rel="stylesheet" href="https://fonts.googleapis.com/css2?family=Great+Vibes&family=Cormorant+SC:wght@500&family=Roboto+Condensed:wght@300&display=swap">
<style>
  :root {
    --page: #ffffff;
    --label-blue: #14107a;
    --label-blue-light: #3d4fb8;
    --band-grey: #333333;
    --capsule-blue: #1b8fd0;
    --capsule-blue-dark: #0f6fae;
    --capsule-rim: #0a5f96;
    --silver: #e6e6ea;
    --band-text: #e8e8e8;
  }
  html, body {
    margin: 0;
    padding: 0;
    width: 1200px;
    height: 3403px;
    overflow: hidden;
    background: var(--page);
  }
  .canvas {
    position: relative;
    width: 1200px;
    height: 3403px;
    background: var(--page);
  }

  /* Neck capsule */
  .capsule {
    position: absolute;
    left: 453px;
    top: 90px;
    width: 294px;
    height: 723px;
    background: linear-gradient(90deg, var(--capsule-blue-dark) 0%, var(--capsule-blue) 30%, var(--capsule-blue) 70%, var(--capsule-blue-dark) 100%);
  }
  .capsule-rim {
    position: absolute;
    left: -14px;
    top: 0;
    width: 322px;
    height: 70px;
    background: linear-gradient(180deg, var(--capsule-blue) 0%, var(--capsule-rim) 100%);
    border-radius: 10px 10px 4px 4px;
  }
  .capsule-pattern {
    position: absolute;
    left: 37px;
    top: 130px;
    width: 220px;
    height: 420px;
    border-radius: 50%;
    background: radial-gradient(ellipse at center, rgba(120, 170, 235, 0.45) 0%, rgba(120, 170, 235, 0.15) 55%, rgba(120, 170, 235, 0) 75%);
  }
  .capsule-brand {
    position: absolute;
    left: 0;
    top: 225px;
    width: 100%;
    text-align: center;
    font-family: "Great Vibes", cursive;
    font-size: 40px;
    color: var(--silver);
    opacity: 0.85;
  }

  /* Front label */
  .front-label {
    position: absolute;
    left: 235px;
    top: 1616px;
    width: 730px;
    height: 916px;
    background: var(--label-blue);
  }
  .label-pattern {
    position: absolute;
    left: 40px;
    top: 40px;
    width: 650px;
    height: 620px;
    border-radius: 50%;
    background: radial-gradient(ellipse at center, rgba(90, 120, 210, 0.55) 0%, rgba(90, 120, 210, 0.25) 50%, rgba(90, 120, 210, 0) 72%);
  }
  .brand-name {
    position: absolute;
    left: 0;
    top: 300px;
    width: 100%;
    margin: 0;
    text-align: center;
    font-family: "Great Vibes", cursive;
    font-weight: 400;
    font-size: 118px;
    line-height: 1;
    color: var(--silver);
  }
  .product-name {
    position: absolute;
    left: 0;
    top: 495px;
    width: 100%;
    margin: 0;
    text-align: center;
    font-family: "Cormorant SC", serif;
    font-weight: 500;
    font-size: 56px;
    letter-spacing: 2px;
    color: var(--silver);
  }
  .info-band {
    position: absolute;
    left: 0;
    top: 697px;
    width: 100%;
    height: 169px;
    background: var(--band-grey);
    display: flex;
    flex-direction: column;
    justify-content: center;
    align-items: center;
    font-family: "Roboto Condensed", sans-serif;
    font-weight: 300;
    font-size: 30px;
    line-height: 1.45;
    color: var(--band-text);
  }
  .info-band p { margin: 0; }
</style>
</head>
<body>
<main class="canvas">
  <section class="capsule" aria-label="Neck capsule">
    <div class="capsule-rim"></div>
    <div class="capsule-pattern" role="img" aria-label="Soft starry dot pattern in light blue"></div>
    <div class="capsule-brand">Maple Hollow</div>
  </section>

  <section class="front-label" aria-label="Front label">
    <div class="label-pattern" role="img" aria-label="Soft starry dot pattern in lighter blue"></div>
    <h1 class="brand-name">Maple Hollow</h1>
    <h2 class="product-name">Shiraz 2016</h2>
    <div class="info-band">
      <p>WINE OF AUSTRALIA</p>
      <p>750 ml.</p>
    </div>
  </section>
</main>
</body>
</html>
```